Professional/modern business card design for construction company

We need a new business card design, double sided keeping it modern, sleek, professional and simple. We are an earthmoving business but do not want any pictures of machinery. I would like one side to have the logo and the other to have all the information, keeping with the colors in our logo. The business card will need to be able to be customised so we can use it for several different managers., we would also like to be able to use the design to apply it to other stationary ie. letterheads, notebooks etc. We do not really have a tag line but we could put on there that we specialise in - Agriculture, Civil Construction and Mining.

Contact Information for Business Card

Brolga Ridge Excavations Pty Ltd
ABN 58 402 937 615
82 Gumleaf Creek Road, Moree NSW 2400

Harold Benton
Managing Director
P 0418 639 204
E haroldbenton@brolgaridgeexc.com.au

Font styles to use
Serif
Sans Serif

Requirements
Nice to have
• I have attached some examples of ideas.
Should not have
• images of machinery

```html
<!DOCTYPE html>
<html lang="en">
<head>
<meta charset="utf-8">
<title>Brolga Ridge Excavations – Business Card</title>
<link rel="stylesheet" href="https://fonts.googleapis.com/css2?family=Arimo:wght@400;700&family=Josefin+Sans:wght@300;400&display=swap">
<style>
  :root {
    --backdrop: #e1e1dc;
    --card: #f5f6f7;
    --orange: #f58a21;
    --charcoal: #434343;
    --rule-grey: #8a8a8a;
  }
  * { margin: 0; padding: 0; box-sizing: border-box; }
  html, body { width: 1200px; height: 960px; overflow: hidden; }
  body { background: var(--backdrop); position: relative; font-family: "Arimo", Arial, sans-serif; }

  .card {
    position: absolute;
    width: 558px;
    height: 307px;
    background: var(--card);
    box-shadow: 1px 3px 3px rgba(0,0,0,0.18);
    overflow: hidden;
  }
  .card--front { left: 346px; top: 146px; }
  .card--back  { left: 342px; top: 538px; }
  .card__shapes { position: absolute; inset: 0; }

  .wordmark {
    position: absolute;
    color: var(--charcoal);
    font-family: "Arimo", Arial, sans-serif;
    font-weight: 700;
    line-height: 1.05;
    letter-spacing: -0.3px;
  }
  .card--front .wordmark {
    left: 0; right: 0; top: 124px;
    text-align: center;
    font-size: 30px;
  }
  .card--back .wordmark {
    left: 54px; top: 178px; width: 170px;
    font-size: 21px;
  }

  .person {
    position: absolute;
    right: 352px; top: 92px;
    text-align: right;
    color: var(--charcoal);
  }
  .person__name { font-size: 21px; font-weight: 700; line-height: 1; }
  .person__role { font-size: 10px; font-weight: 400; margin-top: 3px; }

  .contact {
    position: absolute;
    left: 270px;
    color: #555;
    font-family: "Josefin Sans", Arial, sans-serif;
    font-weight: 300;
    white-space: nowrap;
  }
  .contact__company { top: 100px; font-size: 12px; }
  .contact__details { top: 131px; font-size: 9px; line-height: 12px; }
  .contact__phone   { top: 194px; left: 273px; font-size: 13px; }
  .contact__email   { top: 213px; left: 273px; font-size: 9px; }
  .contact__label   { font-size: 12px; margin-right: 3px; }
</style>
</head>
<body>

  <section class="card card--front" aria-label="Business card front">
    <svg class="card__shapes" width="558" height="307" viewBox="0 0 558 307">
      <polygon points="0,0 94,0 0,307" fill="var(--orange)"/>
      <polygon points="558,0 558,307 462,307" fill="var(--charcoal)"/>
    </svg>
    <div class="wordmark">Brolga Ridge<br>Excavations</div>
  </section>

  <section class="card card--back" aria-label="Business card back">
    <svg class="card__shapes" width="558" height="307" viewBox="0 0 558 307">
      <polygon points="0,0 558,0 0,60" fill="var(--orange)"/>
      <polygon points="558,247 558,307 0,307" fill="var(--charcoal)"/>
      <polyline points="258,56 258,88 558,88" fill="none" stroke="var(--orange)" stroke-width="1"/>
      <polyline points="258,268 258,242 558,242" fill="none" stroke="var(--rule-grey)" stroke-width="1"/>
    </svg>

    <div class="person">
      <div class="person__name">Harold Benton</div>
      <div class="person__role">Diretor-gerente</div>
    </div>

    <div class="wordmark">Brolga Ridge<br>Excavations</div>

    <div class="contact contact__company">Brolga Ridge Excavations Pty Ltd</div>
    <div class="contact contact__details">
      ABN 58 402 937 615<br>
      82 Gumleaf Creek Road, Moree NSW<br>
      2400
    </div>
    <div class="contact contact__phone">P 0418 639 204</div>
    <div class="contact contact__email"><span class="contact__label">E</span>haroldbenton@brolgaridgeexc.com.au</div>
  </section>

</body>
</html>
```